Income Tax Flyer - Updates Needed

Just need to update this flyer design and give it a new look. We would like to keep all the same wording but make it stand out a little more. Our selling point is the "Same Day Tax Advance up to $6,000"

Industry/Entity Type

Lending, Small Loans, Tax Services, Title Loans, Personal Loans

```html
<!DOCTYPE html>
<html lang="en">
<head>
<meta charset="utf-8">
<title>Tax Advance Flyer</title>
<link href="https://fonts.googleapis.com/css2?family=Bebas+Neue&family=Quicksand:wght@500;600;700&display=swap" rel="stylesheet">
<style>
  :root {
    --page-bg: #f6f6f6;
    --paper: #ececec;
    --brand-red: #c8202c;
    --brand-green: #4e9b47;
    --deep-green: #173619;
    --ink: #1e1e1e;
    --white: #f4f4f4;
  }
  * { margin: 0; padding: 0; box-sizing: border-box; }
  html, body { width: 1200px; height: 1200px; overflow: hidden; background: var(--page-bg); }
  .flyer {
    position: absolute; left: 186px; top: 20px; width: 828px; height: 1160px;
    background: var(--paper); overflow: hidden;
    font-family: "Quicksand", "Varela Round", sans-serif;
  }
  .header { position: absolute; left: 0; top: 0; width: 100%; height: 135px; }
  .brand {
    position: absolute; left: 39px; top: 50px;
    display: flex; align-items: center; gap: 10px;
    color: var(--deep-green); font-weight: 700; font-size: 28px;
  }
  .brand-dot { width: 16px; height: 16px; border-radius: 50%; background: var(--brand-red); }
  .tagline {
    position: absolute; right: 40px; top: 34px; text-align: right; font-weight: 700; line-height: 1.3;
  }
  .tagline .line-1 { color: var(--brand-red); font-size: 30px; }
  .tagline .line-2 { color: var(--brand-green); font-size: 34px; }
  .hero-photo {
    position: absolute; left: 0; top: 135px; width: 100%; height: 522px;
    background: linear-gradient(90deg, #8d98a4 0%, #c9d2d8 25%, #a9b4bf 55%, #d6dde2 80%, #9aa6b1 100%);
  }
  .offer-band { position: absolute; left: 0; top: 657px; width: 100%; height: 301px; background: var(--deep-green); }
  .offer-box {
    position: absolute; left: 79px; top: 548px; width: 671px; height: 225px;
    background: var(--brand-green); color: var(--white);
    font-family: "Bebas Neue", "Oswald", sans-serif; text-align: center;
    display: flex; flex-direction: column; justify-content: center;
  }
  .offer-box .offer-lead { font-size: 88px; line-height: 86px; letter-spacing: 1px; }
  .offer-box .offer-amount { font-size: 92px; line-height: 90px; letter-spacing: 1px; }
  .benefits { position: absolute; left: 0; top: 799px; width: 100%; }
  .benefit {
    position: absolute; width: 220px; margin-left: -110px; text-align: center;
    color: var(--white); font-weight: 600; font-size: 19px; line-height: 27px;
  }
  .benefit svg { display: block; margin: 0 auto 22px; }
  .benefit-1 { left: 165px; } .benefit-2 { left: 432px; } .benefit-3 { left: 697px; }
  .cta {
    position: absolute; left: 0; top: 966px; width: 100%; text-align: center;
    color: var(--brand-red); font-weight: 700; font-size: 64px; line-height: 70px;
  }
  .divider { position: absolute; left: 0; top: 1050px; width: 100%; height: 2px; background: var(--brand-green); }
  .address { position: absolute; left: 39px; top: 1062px; font-size: 23px; line-height: 29px; }
  .address .addr-1 { color: var(--brand-green); font-weight: 700; }
  .address .addr-2 { color: var(--ink); font-weight: 500; }
  .phone { position: absolute; right: 40px; top: 1062px; text-align: right; }
  .phone .phone-label { color: var(--brand-green); font-weight: 700; font-size: 23px; line-height: 29px; }
  .phone .phone-number { color: var(--ink); font-weight: 700; font-size: 31px; line-height: 34px; }
</style>
</head>
<body>
<div class="flyer">
  <header class="header">
    <div class="brand"><span class="brand-dot"></span><span>Ledgerline</span></div>
    <div class="tagline">
      <div class="line-1">File your taxes and Apply fo an</div>
      <div class="line-2">Easy Advance!</div>
    </div>
  </header>

  <div class="hero-photo" role="img" aria-label="Photo of two smiling businesswomen in grey suits standing in a bright office lobby"></div>
  <div class="offer-band"></div>

  <div class="offer-box">
    <div class="offer-lead">Apply here for</div>
    <div class="offer-amount">$5,000-$6,000 today!</div>
  </div>

  <div class="benefits">
    <div class="benefit benefit-1">
      <svg width="60" height="60" viewBox="0 0 60 60">
        <circle cx="30" cy="30" r="30" fill="var(--brand-green)"/>
        <g fill="none" stroke="#f4f4f4" stroke-width="2" stroke-linecap="round">
          <circle cx="30" cy="33" r="14"/>
          <line x1="30" y1="19" x2="30" y2="15"/><line x1="26" y1="14" x2="34" y2="14"/>
          <line x1="41" y1="22" x2="44" y2="19"/>
        </g>
        <text x="30" y="38" text-anchor="middle" font-size="14" font-weight="700" fill="#f4f4f4" font-family="Quicksand, sans-serif">$</text>
      </svg>
      Available in<br>24 Hours of Less
    </div>
    <div class="benefit benefit-2">
      <svg width="60" height="60" viewBox="0 0 60 60">
        <circle cx="30" cy="30" r="30" fill="var(--brand-green)"/>
        <circle cx="27" cy="26" r="13" fill="none" stroke="#f4f4f4" stroke-width="2"/>
        <text x="27" y="31" text-anchor="middle" font-size="13" font-weight="700" fill="#f4f4f4" font-family="Quicksand, sans-serif">$</text>
        <path d="M33 33 v-6 a2 2 0 0 1 4 0 v8 l5 1 a3 3 0 0 1 2 4 l-2 6 h-9 l-4 -6" fill="var(--brand-green)" stroke="#f4f4f4" stroke-width="2" stroke-linejoin="round"/>
      </svg>
      Choose You<br>Loan Amount
    </div>
    <div class="benefit benefit-3">
      <svg width="60" height="60" viewBox="0 0 60 60">
        <circle cx="30" cy="30" r="30" fill="var(--brand-green)"/>
        <rect x="26" y="13" width="16" height="26" rx="2" fill="none" stroke="#f4f4f4" stroke-width="2" transform="rotate(12 34 26)"/>
        <text x="34" y="31" text-anchor="middle" font-size="12" font-weight="700" fill="#f4f4f4" font-family="Quicksand, sans-serif">$</text>
        <path d="M17 46 l4 -12 l8 -4 a2 2 0 0 1 2 3 l-5 4 l6 -1 a2 2 0 0 1 1 4 l-8 4 l-3 4" fill="var(--brand-green)" stroke="#f4f4f4" stroke-width="2" stroke-linejoin="round"/>
      </svg>
      Quick and<br>Easy
    </div>
  </div>

  <div class="cta">Contact Us Today!</div>
  <div class="divider"></div>

  <div class="address">
    <div class="addr-1">Address Line 1</div>
    <div class="addr-2">Address Line 2</div>
  </div>
  <div class="phone">
    <div class="phone-label">Phoen Number</div>
    <div class="phone-number">0123 456 789</div>
  </div>
</div>
</body>
</html>
```